Travel video blogger needs website design

I need a website designed for my new travel video blog "Roaming Compass". I have only just started but need a website that is fairly simple and not too busy. I have a logo which I want on it (I have attached it to this project). I also want a link to all my other social medias on the main page (vidstreamhub, Snapmosaic and friendweave) and my videos as well. Here is a link to my vidstreamhub page for you to look at: https://www.vidstreamhub.example/channel/QXr7mPzT2wVn84KsdYe31jaB
As I have only just started and I am still trying to find my specific niche, again I need it to be sleek and simple that I can go in and change slightly here and there. I would like these pages on the website: About Me, Videos, Social Media, Blog, Gallery, contact me. for an example I like the look of www.wanderingkinfolk.example website.

I already have the domain and I am with Nestwarp with wordpress.org. I just want to spend my time getting better and learning about videos then trying to create a website (I am a bit of a perfectionist when I try to do something).

I

Target Market(s)

Young Adults (majority females) between the ages of 18 and 30 with an interest in travelling.

Industry/Entity Type

Travel Industry

Number of Pages Required

1 page

Colors

Designer to choose colors to be used in the design.

Requirements
Must have
• A like to my Snapmosaic, friendweave and vidstreamhub channels on the home page
• Must be a nice, simple design
• Must have my logo on the front and name "Roaming Compass"
Nice to have
• A nice light, bright coloured theme
Should not have
• A dark coloured theme

```html
<!DOCTYPE html>
<html lang="en">
<head>
<meta charset="utf-8">
<title>Roaming Compass — Travel Video Blog</title>
<link rel="stylesheet" href="https://fonts.googleapis.com/css2?family=Mulish:wght@300;400;600&family=Open+Sans:wght@400&display=swap">
<style>
  :root{
    --ink:#222;
    --text:#555;
    --muted:#777;
    --rule:#bdbdbd;
    --card:#ebebeb;
    --footer:#efefef;
    --white:#fff;
  }
  *{box-sizing:border-box;margin:0;padding:0}
  html,body{width:1200px;height:2546px;overflow:hidden;background:var(--white)}
  body{position:relative;font-family:"Mulish",sans-serif;color:var(--ink)}
  a{color:inherit;text-decoration:none}
  .abs{position:absolute}

  /* Header */
  .brand{left:132px;top:16px;width:140px;text-align:center}
  .brand-mark{display:block;width:56px;height:56px;border:3px solid var(--ink);border-radius:50%;margin:0 auto 8px}
  .brand-name{font-size:15px;font-weight:600;letter-spacing:.5px;white-space:nowrap;text-transform:uppercase}
  .social-top{right:134px;top:34px;display:flex;gap:16px;font-size:12px;color:var(--muted);font-family:"Open Sans",sans-serif}
  .main-nav{right:134px;top:93px;display:flex;gap:36px;font-size:13px;letter-spacing:.3px;color:var(--muted);text-transform:uppercase}
  .main-nav .active{color:var(--ink);border-bottom:1.5px solid var(--ink);padding-bottom:3px}

  /* Hero */
  .hero{left:132px;top:139px;width:934px;height:475px;
    background:linear-gradient(100deg,#c9c3b8 0%,#d9cbb6 35%,#c9a987 60%,#c98e52 78%,#b9824e 100%)}
  .hero-title{left:168px;top:346px;font-size:40px;font-weight:300;line-height:48px;color:#1a1a1a}
  .hero-btn{left:168px;top:465px;width:111px;height:41px;background:var(--white);font-size:13px;display:flex;align-items:center;justify-content:center;text-transform:uppercase;color:var(--ink)}
  .hero-dots{left:555px;top:581px;display:flex;gap:10px}
  .hero-dots span{width:15px;height:15px;border:2px solid #222;border-radius:50%}
  .hero-dots span.on{background:radial-gradient(circle,#222 40%,transparent 45%)}

  /* Intro */
  .section-title{left:0;width:1200px;text-align:center;font-size:33px;font-weight:300;color:#111}
  .intro{left:132px;top:730px;width:934px;text-align:center;font-family:"Open Sans",sans-serif;font-size:14.5px;line-height:26px;color:var(--text)}
  .rule{left:132px;width:934px;height:1px;background:var(--rule)}

  /* Videos */
  .video{width:219px}
  .video-thumb{position:relative;width:219px;height:210px}
  .video-thumb svg{position:absolute;left:95px;top:91px}
  .video-caption{text-align:center;font-size:16px;margin-top:6px;color:#111}
  .view-all{left:545px;top:1836px;width:110px;height:39px;border:1px solid #555;font-size:12.5px;display:flex;align-items:center;justify-content:center;color:var(--ink)}

  /* Blog */
  .blog-card{top:2103px;width:443px;height:229px;background:var(--card)}
  .blog-image{position:absolute;left:0;top:0;width:193px;height:229px}
  .blog-body{position:absolute;left:220px;top:16px;width:205px}
  .blog-title{font-size:15.5px;line-height:22px;color:#111}
  .blog-text{margin-top:12px;font-family:"Open Sans",sans-serif;font-size:10.5px;line-height:17px;color:var(--text)}
  .blog-btn{position:absolute;left:220px;top:175px;width:87px;height:27px;border:1px solid #888;font-size:10.5px;color:var(--muted);display:flex;align-items:center;justify-content:center}
  .arrow{top:2200px}

  /* Footer */
  .site-footer{left:0;top:2413px;width:1200px;height:133px;background:var(--footer)}
  .footer-nav{left:132px;top:2455px;font-size:12.5px;color:#333;word-spacing:2px}
  .footer-nav i{font-style:normal;margin:0 8px;color:#555}
  .copyright{left:132px;top:2486px;font-size:12.5px;color:#333}
  .social-footer{right:134px;top:2471px;display:flex;gap:16px;font-size:12px;color:var(--muted);font-family:"Open Sans",sans-serif}
</style>
</head>
<body>

<header>
  <a class="abs brand" href="#"><span class="brand-mark"></span><span class="brand-name">Roaming Compass</span></a>
  <nav class="abs social-top"><a href="#">friendweave</a><a href="#">vidstreamhub</a><a href="#">Snapmosaic</a></nav>
  <nav class="abs main-nav">
    <a class="active" href="#">Home</a><a href="#">About Me</a><a href="#">Videos</a><a href="#">Social Media</a><a href="#">Blog</a><a href="#">Gallery</a><a href="#">Contact Me</a>
  </nav>
</header>

<section>
  <div class="abs hero" role="img" aria-label="Photo of a smiling traveller on a sandy beach by the sea"></div>
  <h1 class="abs hero-title">Maecenas tortor<br>accumsan quam varius</h1>
  <a class="abs hero-btn" href="#">Read More</a>
  <div class="abs hero-dots"><span class="on"></span><span></span><span></span><span></span></div>
</section>

<section>
  <h2 class="abs section-title" style="top:684px">Phasellus nisl condimentum</h2>
  <p class="abs intro">Nulla tristique posuere molestie. Aliquam erat volutpat. Etiam quis aliquet risus. Duis ornare erat eget magna dapibus, in accumsan quam pharetra. Nam tempus, quam in bibendum vulputate, sapien dolor viverra nisl, vitae euismod elit turpis et nulla. Aliquam erat volutpat. Pellentesque blandit lacus eget nunc faucibus, et tincidunt eros viverra. Phasellus consequat sagittis nisi suscipit feugiat. Cras eget leo sed nunc hendrerit ultricies eu at nisl. Praesent iaculis faucibus urna sit amet lacinia.</p>
  <div class="abs rule" style="top:908px"></div>
</section>

<section>
  <h2 class="abs section-title" style="top:978px">Videos</h2>

  <div class="abs video" style="left:132px;top:1040px"><div class="video-thumb" role="img" aria-label="Video still of two children by a red tent" style="background:linear-gradient(160deg,#6b6b6b,#2d2a2a 55%,#8a3a32)"><svg width="30" height="30" viewBox="0 0 30 30"><circle cx="15" cy="15" r="15" fill="#fff"/><path d="M12 9l9 6-9 6z" fill="#222"/></svg></div><div class="video-caption">Aliquam consectetur</div></div>
  <div class="abs video" style="left:371px;top:1040px"><div class="video-thumb" role="img" aria-label="Video still of scuba divers underwater" style="background:linear-gradient(170deg,#2c8a98,#1a6670 60%,#0f4a52)"><svg width="30" height="30" viewBox="0 0 30 30"><circle cx="15" cy="15" r="15" fill="#fff"/><path d="M12 9l9 6-9 6z" fill="#222"/></svg></div><div class="video-caption">Proin eget</div></div>
  <div class="abs video" style="left:610px;top:1040px"><div class="video-thumb" role="img" aria-label="Video still of a sunset over ocean waves" style="background:linear-gradient(180deg,#1b2444,#5a4a6a 40%,#d0784a 55%,#2c3850 80%,#6a6058)"><svg width="30" height="30" viewBox="0 0 30 30"><circle cx="15" cy="15" r="15" fill="#fff"/><path d="M12 9l9 6-9 6z" fill="#222"/></svg></div><div class="video-caption">Fusce eget</div></div>
  <div class="abs video" style="left:849px;top:1040px"><div class="video-thumb" role="img" aria-label="Video still of an autumn forest path" style="background:linear-gradient(180deg,#6f6a1e,#9a6a22 50%,#7a4a1a)"><svg width="30" height="30" viewBox="0 0 30 30"><circle cx="15" cy="15" r="15" fill="#fff"/><path d="M12 9l9 6-9 6z" fill="#222"/></svg></div><div class="video-caption">Vestibulum</div></div>

  <div class="abs video" style="left:132px;top:1305px"><div class="video-thumb" role="img" aria-label="Video still of a hiker facing snowy mountains at dusk" style="background:linear-gradient(180deg,#2a3a66,#d58c4e 35%,#5a5a5c 60%,#3a3a3c)"><svg width="30" height="30" viewBox="0 0 30 30"><circle cx="15" cy="15" r="15" fill="#fff"/><path d="M12 9l9 6-9 6z" fill="#222"/></svg></div><div class="video-caption">Pellentesque</div></div>
  <div class="abs video" style="left:371px;top:1305px"><div class="video-thumb" role="img" aria-label="Video still of a camel caravan in desert dunes" style="background:linear-gradient(180deg,#7aa2bd,#d6b27a 35%,#c08a45)"><svg width="30" height="30" viewBox="0 0 30 30"><circle cx="15" cy="15" r="15" fill="#fff"/><path d="M12 9l9 6-9 6z" fill="#222"/></svg></div><div class="video-caption">Fusce sollicitudin</div></div>
  <div class="abs video" style="left:610px;top:1305px"><div class="video-thumb" role="img" aria-label="Video still of a traveller under palm trees at sunset" style="background:linear-gradient(180deg,#c88a5a,#d6a37a 40%,#4a2e22 80%)"><svg width="30" height="30" viewBox="0 0 30 30"><circle cx="15" cy="15" r="15" fill="#fff"/><path d="M12 9l9 6-9 6z" fill="#222"/></svg></div><div class="video-caption">Proin placerat</div></div>
  <div class="abs video" style="left:849px;top:1305px"><div class="video-thumb" role="img" aria-label="Video still of surfers walking on a beach at sunset" style="background:linear-gradient(180deg,#d89a7a,#e6a05a 45%,#b86a3a)"><svg width="30" height="30" viewBox="0 0 30 30"><circle cx="15" cy="15" r="15" fill="#fff"/><path d="M12 9l9 6-9 6z" fill="#222"/></svg></div><div class="video-caption">Maecenas vel</div></div>

  <div class="abs video" style="left:132px;top:1570px"><div class="video-thumb" role="img" aria-label="Video still of a yak before mountains" style="background:linear-gradient(180deg,#1e3a6e,#5a7aa0 40%,#8a6a4a 70%,#5a3a2a)"><svg width="30" height="30" viewBox="0 0 30 30"><circle cx="15" cy="15" r="15" fill="#fff"/><path d="M12 9l9 6-9 6z" fill="#222"/></svg></div><div class="video-caption">Aenean facilisis</div></div>
  <div class="abs video" style="left:371px;top:1570px"><div class="video-thumb" role="img" aria-label="Video still of beach umbrellas by turquoise water" style="background:linear-gradient(180deg,#3a5a9a,#c4d4e4 40%,#3ab0b8 55%,#e4e0d6 75%)"><svg width="30" height="30" viewBox="0 0 30 30"><circle cx="15" cy="15" r="15" fill="#fff"/><path d="M12 9l9 6-9 6z" fill="#222"/></svg></div><div class="video-caption">Vivamus efficitur</div></div>
  <div class="abs video" style="left:610px;top:1570px"><div class="video-thumb" role="img" aria-label="Video still of a kayaker in white water rapids" style="background:linear-gradient(160deg,#3a4a3a,#7a8a80 40%,#c8c0a0 60%,#4a5a48)"><svg width="30" height="30" viewBox="0 0 30 30"><circle cx="15" cy="15" r="15" fill="#fff"/><path d="M12 9l9 6-9 6z" fill="#222"/></svg></div><div class="video-caption">Sed tellus</div></div>
  <div class="abs video" style="left:849px;top:1570px"><div class="video-thumb" role="img" aria-label="Video still of a hiker on a green misty hillside" style="background:linear-gradient(180deg,#c8ccc8,#7a9a6a 40%,#4a6a3a)"><svg width="30" height="30" viewBox="0 0 30 30"><circle cx="15" cy="15" r="15" fill="#fff"/><path d="M12 9l9 6-9 6z" fill="#222"/></svg></div><div class="video-caption">Etiam mattis</div></div>

  <a class="abs view-all" href="#">View All</a>
  <div class="abs rule" style="top:1965px"></div>
</section>

<section>
  <h2 class="abs section-title" style="top:2035px">Blog</h2>

  <svg class="abs arrow" style="left:54px" width="18" height="30" viewBox="0 0 18 30"><path d="M15 3L4 15l11 12" fill="none" stroke="#666" stroke-width="2.5"/></svg>
  <svg class="abs arrow" style="left:1128px" width="18" height="30" viewBox="0 0 18 30"><path d="M3 3l11 12L3 27" fill="none" stroke="#666" stroke-width="2.5"/></svg>

  <article class="abs blog-card" style="left:132px">
    <div class="blog-image" role="img" aria-label="Photo of a canal city lit up at night" style="background:linear-gradient(180deg,#2a3a5a,#c8783a 45%,#e0a040 70%,#3a2a1a)"></div>
    <div class="blog-body">
      <h3 class="blog-title" style="font-weight:400">Etiam mattis augue vehicula odio posuere, sit amet</h3>
      <p class="blog-text">Etiam mattis augue vehicula odio posuere, sit amet tempus lectus luctus. Nulla facilisi. Etiam vel massa elementum, bibendum tellus venenatis, feugiat massa.</p>
    </div>
    <a class="blog-btn" href="#">Read More</a>
  </article>

  <article class="abs blog-card" style="left:624px">
    <div class="blog-image" role="img" aria-label="Photo of a traveller working on a laptop on a tropical balcony" style="background:linear-gradient(160deg,#4a8a3a,#9ac46a 40%,#8a6a4a 75%,#5a4030)"></div>
    <div class="blog-body">
      <h3 class="blog-title" style="font-weight:400">Curabitur venenatis lacinia ornare. Cras sollicitudin</h3>
      <p class="blog-text">Etiam mattis augue vehicula odio posuere, sit amet tempus lectus luctus. Nulla facilisi. Etiam vel massa elementum, bibendum tellus venenatis, feugiat massa.</p>
    </div>
    <a class="blog-btn" href="#">Read More</a>
  </article>
</section>

<footer>
  <div class="abs site-footer"></div>
  <nav class="abs footer-nav"><a href="#">Home</a><i>|</i><a href="#">About Me</a><i>|</i><a href="#">Videos</a><i>|</i><a href="#">Social Media</a><i>|</i><a href="#">Blog</a><i>|</i><a href="#">Gallery</a><i>|</i><a href="#">Contact Me</a></nav>
  <p class="abs copyright">Copyright&nbsp; ©&nbsp; 2018&nbsp; Roaming Compass.&nbsp;&nbsp; All rights reserved.</p>
  <nav class="abs social-footer"><a href="#">friendweave</a><a href="#">vidstreamhub</a><a href="#">Snapmosaic</a></nav>
</footer>

</body>
</html>
```